Business card design for web travel company

Hi
we'd like to receive some proposal for a business card design.
Quindra is a private travel club, dedicated to all travel lovers, with unique offers for exclusive destinations all around the world. At Quindra you can find a wide range of offers for resorts, boutique hotels and travel packages at the best guaranteed price available on the market. The convenience of the offer is guaranteed by a private sales model: offers are available for a limited time only and they are personally chosen by Quindra's qualified team of travel experts.
We offer only exclusive hotels with discounted prices but we are not an outlet or a discount supermarket: the design should reflect our connection with luxury, exclusivity using the same style of our website www.quindra-example.com.
We want to make sure that when we'll present ourself to our business partner they will feel immediately which is our brand positioning giving them also a sense of an affordable and reliable partner.
In attachment you can also find our brand guidelines (please note that we are NOT USING ANY MORE THE TAG LINE "Five star outlet" mentioned in it).
The info to be inserted are:
Name Surname
Job Title
Tel
Mobile (when needed)
Email
Quindra S.r.l.
Via Pietro Lanzi 27
20137 Milano

```html
<!DOCTYPE html>
<html lang="it">
<head>
<meta charset="utf-8">
<title>Quindra – Business Card</title>
<link rel="stylesheet" href="https://fonts.googleapis.com/css2?family=Arimo:wght@400;700&display=swap">
<style>
  :root {
    --paper: #ffffff;
    --frame: #3a3a3a;
    --card: #2b2b2b;
    --card-light: #4a4a4a;
    --band-dark: #262626;
    --white: #ffffff;
    --gold: #c9ac5f;
    --title-box: #454545;
  }
  * { margin: 0; padding: 0; box-sizing: border-box; }
  html, body { width: 1075px; height: 1200px; overflow: hidden; background: var(--paper); }
  body { font-family: "Arimo", Arial, sans-serif; position: relative; }

  .sheet-frame {
    position: absolute; left: 2px; top: 2px; width: 1071px; height: 1196px;
    border: 2px solid var(--frame);
  }

  .card {
    position: absolute; width: 810px; background: var(--card); overflow: hidden;
    box-shadow: 0 4px 12px rgba(0,0,0,0.25);
  }

  /* Front */
  .card-front { left: 123px; top: 88px; height: 493px; }
  .card-front .texture {
    position: absolute; inset: 0;
    background: radial-gradient(ellipse at 50% 48%, #5a5a5a 0%, #333 45%, #272727 100%);
  }
  .card-front .brand-name {
    position: absolute; left: 0; right: 0; top: 50%; transform: translateY(-50%);
    text-align: center; color: var(--white);
    font-size: 106px; font-weight: 400; letter-spacing: 1px; line-height: 1;
  }

  /* Back */
  .card-back { left: 127px; top: 633px; height: 496px; }
  .card-back .header-band {
    position: absolute; left: 0; top: 0; width: 100%; height: 141px;
    background: linear-gradient(180deg, #2e2e2e 0%, var(--band-dark) 100%);
  }
  .card-back .header-rule {
    position: absolute; left: 0; top: 139px; width: 100%; height: 4px;
    background: linear-gradient(90deg, #3a3a3a 0%, #9a9a9a 40%, #f2f2f2 70%, #6a6a6a 100%);
  }
  .card-back .brand-name-small {
    position: absolute; left: 49px; top: 66px; color: var(--white);
    font-size: 40px; font-weight: 400; line-height: 1; letter-spacing: 0.5px;
  }

  .company-address {
    position: absolute; left: 45px; top: 186px; color: var(--white);
    font-size: 20px; line-height: 30px; font-style: normal;
  }
  .contact-list {
    position: absolute; left: 45px; top: 318px; color: var(--white);
    font-size: 20px; line-height: 29px; list-style: none;
  }
  .contact-list .label { color: var(--gold); font-weight: 700; margin-right: 6px; }

  .column-divider {
    position: absolute; left: 358px; top: 163px; width: 4px; height: 305px;
    background: var(--white);
  }

  .person-name {
    position: absolute; left: 380px; top: 184px; color: var(--white);
    font-size: 36px; font-weight: 700; line-height: 1.1;
  }
  .job-title {
    position: absolute; left: 382px; top: 249px; width: 295px; height: 37px;
    background: var(--title-box); color: var(--gold);
    font-size: 16px; line-height: 37px; padding-left: 16px; text-transform: uppercase;
  }
</style>
</head>
<body>
  <div class="sheet-frame"></div>

  <section class="card card-front">
    <div class="texture" role="img" aria-label="Dark diagonal pinstripe texture with soft central glow"></div>
    <div class="brand-name">Quindra</div>
  </section>

  <section class="card card-back">
    <div class="header-band" role="img" aria-label="Dark diagonal pinstripe texture band"></div>
    <div class="header-rule"></div>
    <div class="brand-name-small">Quindra</div>

    <address class="company-address">
      Quindra S.r.l.<br>
      Via Pietro Lanzi 27<br>
      20137 Milano
    </address>

    <ul class="contact-list">
      <li><span class="label">Tel</span>xxxxxxxxxxxxxx</li>
      <li><span class="label">Mobile</span>xxxxxxxxxxxxxx</li>
      <li><span class="label">Email</span>xxxxxxxxxxxxxx</li>
    </ul>

    <div class="column-divider"></div>

    <h1 class="person-name">Name Surname</h1>
    <div class="job-title">Job Title</div>
  </section>
</body>
</html>
```